I need a book cover for my book titled Sunny Porch! The subtitle is Quiet Orchard Days and the the author is Marisol Dunleavy. I want the attached photo included on the cover, plus the words "I never met a chicken wing I didn't like!" The book size is 5.06 x 7.81 in. and is 146 pages. For the color scheme, I like a chocolate brown cover with aqua blue letters. (Please note that you don't have to use these colors. Feel free to use this color scheme or whatever you colors you like!)

• Please include my photo for the back cover, along with this text:

Sunny Porch! I was tired of being tired! I was tired of acid reflux, body stiffness, and being overweight. To make matters worse, I suffered from back pain, constipation, leg pain, and lack of sleep. If you are tired of looking to medical test for your answers, this is the book for you. The key was the day I decided to make “me” a priority by being #1 on my “to-do” list.

Our healthcare system seems to be more concerned about treating illness than they are about preventing it; which is why we have so many problems with our health and wellness. That’s why I’m going to give you insights into nutrition, health care, and the pharmaceutical industry.

I’m also going to give you some insights into exercise, supplements, detoxing and essential oils; as well as what goes into your grocery cart and the foods you feed your family.

Because you’re reading this I know you’re ready to live your best life, Sunny Porch! is for you.

Here’s to a healthy you!

Here's a brief bio about the author for the back cover:

Marisol lives in Chicago with her husband, Dr. Wendell, and has three adult children. She is probably one of the most private people you will meet – BUT HAD to tell her story!

```html
<!DOCTYPE html>
<html lang="en">
<head>
<meta charset="utf-8">
<title>Sunny Porch! – Quiet Orchard Days – Book Cover</title>
<link rel="stylesheet" href="https://fonts.googleapis.com/css2?family=Short+Stack&family=Lato:wght@400&family=Archivo:ital,wght@0,400;0,700;1,700&display=swap">
<style>
  :root {
    --chocolate: #582b1e;
    --chocolate-deep: #2a2014;
    --aqua: #27bdbd;
    --gold: #e0a038;
    --tag-gold: #e3a332;
    --spine-grey: #b9b8b7;
    --white: #ffffff;
    --author-brown: #5a2b1c;
  }
  * { margin: 0; padding: 0; box-sizing: border-box; }
  html, body { width: 1200px; height: 891px; overflow: hidden; background: var(--chocolate); }
  .cover { position: relative; width: 1200px; height: 891px; background: var(--chocolate); overflow: hidden; }

  /* Back cover */
  .back { position: absolute; left: 0; top: 0; width: 577px; height: 891px; }
  .author-photo {
    position: absolute; left: 0; top: 138px; width: 247px; height: 347px;
    background: radial-gradient(ellipse at 50% 40%, #8a5a3a 0%, #5a3a22 45%, #3a2616 100%);
  }
  .bio-panel {
    position: absolute; left: 0; top: 485px; width: 247px; height: 288px;
    background: var(--chocolate-deep);
    padding: 32px 20px 0 39px;
  }
  .bio-panel p {
    font-family: "Archivo", Arial, sans-serif; font-size: 17.2px; line-height: 21.6px;
    color: var(--aqua); letter-spacing: 0.2px;
  }
  .back-title {
    position: absolute; left: 250px; width: 300px; top: 138px; text-align: center;
    font-family: "Short Stack", "Comic Sans MS", cursive;
    color: var(--aqua); font-size: 66px; line-height: 68px;
    text-shadow: 2px 3px 4px rgba(0,0,0,0.45);
  }
  .back-subtitle {
    position: absolute; left: 250px; width: 300px; top: 289px; text-align: center;
    font-family: "Archivo", Arial, sans-serif; font-weight: 700; font-size: 18.5px; color: var(--white);
  }
  .blurb {
    position: absolute; left: 282px; top: 370px; width: 255px;
    font-family: "Lato", Arial, sans-serif; font-size: 11.6px; line-height: 15.2px; color: var(--gold);
  }
  .blurb p { margin-bottom: 15.2px; }

  /* Spine */
  .spine {
    position: absolute; left: 577px; top: 0; width: 46px; height: 891px; background: var(--spine-grey);
  }
  .spine-text {
    position: absolute; left: 45px; top: 268px; transform-origin: 0 0; transform: rotate(90deg);
    white-space: nowrap; color: var(--author-brown); display: flex; align-items: baseline; gap: 22px;
  }
  .spine-title { font-family: "Short Stack", "Comic Sans MS", cursive; font-size: 30px; }
  .spine-author { font-family: "Archivo", Arial, sans-serif; font-weight: 700; font-size: 18px; }

  /* Front cover */
  .front { position: absolute; left: 623px; top: 0; width: 577px; height: 891px; }
  .front-photo {
    position: absolute; left: 0; top: 0; width: 577px; height: 770px;
    background:
      radial-gradient(ellipse 90px 80px at 140px 70px, rgba(180,170,60,0.75), transparent),
      radial-gradient(ellipse 160px 90px at 320px 280px, rgba(235,160,110,0.7), transparent),
      radial-gradient(ellipse 120px 120px at 480px 420px, rgba(190,30,35,0.8), transparent),
      radial-gradient(ellipse 200px 150px at 360px 600px, rgba(200,70,30,0.9), transparent),
      radial-gradient(ellipse 260px 200px at 250px 600px, rgba(240,240,240,0.55), transparent),
      radial-gradient(ellipse 60px 90px at 50px 420px, rgba(120,190,70,0.7), transparent),
      linear-gradient(180deg, #5a2b1e 0%, #7a3a24 40%, #6a2a1e 75%, var(--chocolate) 100%);
  }
  .front-title {
    position: absolute; left: 0; width: 577px; top: 40px; text-align: center;
    font-family: "Short Stack", "Comic Sans MS", cursive;
    color: var(--aqua); font-size: 112px; line-height: 112px;
    text-shadow: 3px 4px 6px rgba(0,0,0,0.45);
  }
  .front-subtitle {
    position: absolute; left: 0; width: 577px; top: 287px; text-align: center;
    font-family: "Archivo", Arial, sans-serif; font-weight: 700; font-size: 28px; color: var(--white);
    text-shadow: 1px 2px 3px rgba(0,0,0,0.3);
  }
  .front-author {
    position: absolute; left: 0; width: 577px; top: 346px; text-align: center;
    font-family: "Archivo", Arial, sans-serif; font-weight: 700; font-style: italic; font-size: 17px;
    color: var(--author-brown); letter-spacing: 0.4px;
  }
  .tagline {
    position: absolute; left: 321px; top: 757px;
    font-family: "Archivo", Arial, sans-serif; font-weight: 700; font-size: 26px; line-height: 27px;
    color: var(--tag-gold);
  }
</style>
</head>
<body>
<main class="cover">
  <section class="back">
    <div class="author-photo" role="img" aria-label="Portrait photo of the author, smiling, wearing large gold earrings and a patterned top"></div>
    <div class="bio-panel">
      <p>Marisol lives in Chicago with her husband, Dr. Wendell, and has three adult children. She is probably one of the most private people you will meet – BUT HAD to tell her story!</p>
    </div>
    <h2 class="back-title">Sunny<br>Porch!</h2>
    <p class="back-subtitle">Quiet Orchard Days</p>
    <div class="blurb">
      <p>Sunny Porch! I was tired of being tired! I was tired of acid reflux, body stiffness, and being overweight. To make matters worse, I suffered from back pain, constipation, leg pain, and lack of sleep. If you are tired of looking to medical test for your answers, this is the book for you. The key was the day I decided to make “me” a priority by being #1 on my “to-do” list.</p>
      <p>Our healthcare system seems to be more concerned about treating illness than they are about preventing it; which is why we have so many problems with our health and wellness. That’s why I’m going to give you insights into nutrition, health care, and the pharmaceutical industry.</p>
      <p>I’m also going to give you some insights into exercise, supplements, detoxing and essential oils; as well as what goes into your grocery cart and the foods you feed your family.</p>
      <p>Because you’re reading this I know you’re ready to live your best life, Sunny Porch! is for you.</p>
      <p>Here’s to a healthy you!</p>
    </div>
  </section>

  <section class="spine">
    <div class="spine-text">
      <span class="spine-title">Sunny Porch!</span>
      <span class="spine-author">Marisol Dunleavy.</span>
    </div>
  </section>

  <section class="front">
    <div class="front-photo" role="img" aria-label="Photo of glazed chicken wings on a white dish with celery, carrot sticks and a cup of dip, against a blurred warm background"></div>
    <h1 class="front-title">Sunny<br>Porch!</h1>
    <p class="front-subtitle">Quiet Orchard Days</p>
    <p class="front-author">Marisol Dunleavy.</p>
    <p class="tagline">I never met<br>a chicken wing<br>I didn't like!</p>
  </section>
</main>
</body>
</html>
```